Velvet Root Studio- An All Natural Hair & Skincare Company needs a website design.

Velvet Root Studio is an all-natural Hair & Skin Company that provides all natural hair and skin care products to the ever growing natural hair community. Our primary target market is African American women between the ages of 16-50. I would like my website to be setup in a way that allows me to add photos, and products for sale easily. The site should be very user friendly but clean and professional looking. I have uploaded our new company Logo and I would definitely like it used throughout the pages. Ideally, the site should display our Motto, Company Vision, Pictures of Products and Results of use of products, testimonials from customers, Video tutorials. I need to be able to capture email addresses for easy email blasts and customer data collection, contact info, links to social media accounts, and detailed analytics to track traffic etc. I also need direct links to my CoinPouch and email.

It appears my brief is unclear. This is our first site. So i would like it to be able to showcase and all my products. I would like the coding for easy changes after the site goes live. I am not super tech savvy, but would like to be able to add new products and track traffic. Please let me know if this still needs clarification.

```html
<!DOCTYPE html>
<html lang="en">
<head>
<meta charset="utf-8">
<title>Velvet Root Studio — Natural Hair &amp; Skin Care</title>
<link href="https://fonts.googleapis.com/css2?family=Lato:ital,wght@0,400;0,700;0,900;1,400;1,700;1,900&family=Oswald:wght@400;500&display=swap" rel="stylesheet">
<style>
:root{
  --brown-dark:#4a403b;
  --brown-mid:#5a4d46;
  --orange:#f08a12;
  --gold-top:#c99656;
  --gold-bottom:#a8712f;
  --grey-box:#ececec;
  --text-body:#4a4a4a;
  --white:#ffffff;
  --line:#8a7d75;
}
*{box-sizing:border-box;margin:0;padding:0}
html,body{width:684px;height:1200px;overflow:hidden;background:var(--white)}
body{position:relative;font-family:'Lato',sans-serif;color:var(--text-body)}
.abs{position:absolute}

/* header */
.site-header{left:0;top:0;width:684px;height:62px;background:var(--brown-dark)}
.social{left:360px;top:9px;display:flex;gap:5px}
.social span{width:18px;height:18px;border-radius:3px;background:#6d605a;border:1px solid #8b7e77}
.util-box{top:8px;height:21px;border:1px solid #8b7e77;color:var(--white);font-size:7px;display:flex;align-items:center;gap:6px;padding-left:7px}
.account{left:454px;width:75px}
.cart{left:533px;width:76px}
.nav-item{top:46px;font-size:8px;line-height:10px;color:var(--white);text-transform:uppercase;white-space:nowrap}
.nav-item.active{color:var(--orange);font-weight:700}
.nav-flower{left:297px;top:31px;width:11px;height:11px;border-radius:50%;background:var(--orange)}

.logo-card{left:75px;top:0;width:108px;height:138px;background:var(--white);border-radius:0 0 7px 7px;box-shadow:0 2px 4px rgba(0,0,0,.35);z-index:3;text-align:center}
.logo-mark{margin:12px auto 0;width:62px;height:62px;border-radius:50%;background:var(--orange)}
.logo-name{margin-top:14px;font-size:12.5px;line-height:14px;color:#6b5a50}

/* hero */
.hero{left:0;top:62px;width:684px;height:284px;background:linear-gradient(90deg,#8e8985 0%,#7d7874 45%,#6a5f58 60%,#3b2a24 75%,#5a4d47 90%,#8b8682 100%)}
.hero-title{left:88px;top:166px;width:258px;color:var(--white);font-size:17.5px;line-height:25px;font-weight:400;text-shadow:0 1px 2px rgba(0,0,0,.4)}
.hero-title strong{color:var(--orange);font-weight:700;font-size:21px}
.hero-arrow{top:186px}

/* categories */
.category-band{left:0;top:346px;width:684px;height:187px;background:var(--brown-dark)}
.cat-card{top:362px;width:171px;height:155px;background:var(--white)}
.cat-photo{width:171px;height:123px}
.cat-label{height:32px;background:linear-gradient(180deg,var(--gold-top),var(--gold-bottom));color:var(--white);font-size:14px;display:flex;align-items:center;justify-content:space-between;padding:0 8px 0 12px}
.cat-label i{width:11px;height:11px;border-radius:50%;background:rgba(255,255,255,.75);position:relative}
.cat-label i::after{content:"";position:absolute;left:3.5px;top:3px;border-left:4px solid var(--gold-bottom);border-top:2.5px solid transparent;border-bottom:2.5px solid transparent}

/* welcome */
.welcome-title{left:76px;top:552px;display:flex;align-items:center;gap:6px}
.welcome-title .dot{width:22px;height:22px;border-radius:50%;background:var(--orange)}
.welcome-title h2{font-weight:400;font-size:15px;color:var(--orange)}
.welcome-title h2 span{color:#6b5a50}
.welcome-rule{left:75px;top:585px;width:355px;height:1px;background:#e2e2e2}
.welcome-text{left:75px;top:592px;width:358px;font-size:7px;line-height:12px;color:#333}
.btn-more{left:75px;top:648px;width:59px;height:18px;background:var(--brown-dark);color:var(--white);font-size:8px;font-weight:700;border-radius:2px;display:flex;align-items:center;justify-content:center}
.video{left:438px;top:555px;width:171px;height:111px;border:1px solid #ccc;background:linear-gradient(135deg,#e9e3dc,#b8c4a8 55%,#6b7a4a)}
.video-bar{left:438px;top:655px;width:171px;height:11px;background:#1d2430}
.video-play{left:510px;top:592px}

/* reviews */
.reviews-band{left:0;top:687px;width:684px;height:170px;background:var(--brown-dark)}
.reviews-title{left:0;top:702px;width:684px;text-align:center;font-weight:400;font-size:14px;line-height:18px;color:var(--white)}
.reviews-sub{left:0;top:721px;width:684px;text-align:center;font-size:8px;color:#cfc7c2}
.rule-l,.rule-r{top:740px;height:1px;background:var(--line)}
.rule-l{left:203px;width:122px}.rule-r{left:360px;width:121px}
.stars{left:327px;top:734px;color:var(--orange);font-size:9px;letter-spacing:1px}
.quote-box{left:80px;top:758px;width:475px;height:55px;background:#f4f2f0;border-radius:3px}
.quote-tail{left:330px;top:812px}
.quote-mark{left:92px;top:759px;font-size:20px;line-height:20px;color:#b9b2ad;font-weight:900}
.quote-text{left:90px;top:765px;width:430px;font-size:7.2px;line-height:13.5px;font-style:italic;color:#333;text-indent:18px}
.avatar{left:537px;top:754px;width:67px;height:67px;border-radius:50%;border:3px solid #e3d4c5;background:linear-gradient(160deg,#cfd6db,#8b9aa5)}
.quote-name{left:450px;top:826px;font-size:7px;font-weight:700;font-style:italic;color:var(--orange)}

/* features */
.feature{top:872px;width:170px;height:56px;background:var(--grey-box);display:flex;align-items:center;gap:10px;padding-left:14px;font-size:10px;font-weight:900;font-style:italic;color:#4a403b;line-height:14px;text-transform:uppercase}
.feature.gift{background:#f1eeee;box-shadow:inset 0 0 10px rgba(0,0,0,.12);padding-left:40px}

/* footer */
.footer{left:0;top:943px;width:684px;height:257px;background:linear-gradient(180deg,var(--gold-top),var(--gold-bottom))}
.footer-panel{left:75px;top:960px;width:534px;height:226px;background:var(--brown-dark)}
.news-box{left:75px;top:960px;width:208px;height:88px;background:var(--brown-mid)}
.news-title{left:85px;top:970px;font-size:10px;font-weight:400;color:var(--white)}
.news-rule{left:75px;top:987px;width:208px;height:1px;background:#6e625b}
.news-date{left:85px;top:994px;font-size:8px;font-weight:700;color:var(--orange)}
.news-lead{left:85px;top:1006px;font-size:7px;font-weight:700;color:var(--white)}
.news-text{left:85px;top:1018px;font-size:7px;color:#ddd}
.news-more{left:234px;top:1033px;font-size:7.5px;font-style:italic;color:var(--orange);text-decoration:underline}
.promo-strip{left:289px;top:960px;width:320px;height:92px;background:#c9a378}
.promo{top:962px;width:98px;height:86px;background:linear-gradient(160deg,#6a5a4e,#2c2420);display:flex;align-items:center;justify-content:center;color:var(--white);font-family:'Oswald',sans-serif;border:2px solid #3a302b}
.promo-inner{width:80px;height:74px;border:1px solid rgba(255,255,255,.7);display:flex;flex-direction:column;align-items:center;justify-content:center}
.promo b{font-size:22px;font-weight:400;line-height:26px}
.promo b small{font-size:15px}
.promo span{font-size:10px;margin-top:4px}
.col-title{font-size:11px;font-weight:400;color:var(--white)}
.newsletter-input{left:85px;top:1074px;width:150px;height:16px;background:var(--white);font-size:6.5px;font-style:italic;color:#999;padding:4px}
.newsletter-go{left:240px;top:1074px;width:24px;height:16px;background:var(--orange);color:var(--white);font-size:8px;font-weight:900;text-align:center;line-height:16px}
.store-line{font-size:7px;color:#ddd;line-height:9px}
.links{font-size:7px;color:#eee;line-height:9px}
.links li{list-style:none;position:relative;padding-left:8px}
.links li::before{content:"›";position:absolute;left:0;top:-1px;color:#bbb}
.footer-rule{left:75px;top:1161px;width:534px;height:1px;background:#6e625b}
.copyright{left:87px;top:1167px;font-size:7px;color:#ddd}
.pay{top:1163px;height:16px;width:26px;background:var(--white);border-radius:2px;font-size:5.5px;font-weight:700;color:#4a403b;display:flex;align-items:center;justify-content:center}
</style>
</head>
<body>

<header class="abs site-header"></header>
<div class="abs social" aria-label="Social links">
  <span aria-label="Friendsy"></span><span aria-label="Chirper"></span><span aria-label="Linkly"></span><span aria-label="Circlo"></span>
</div>
<div class="abs util-box account">
  <svg width="14" height="12" viewBox="0 0 14 12"><circle cx="7" cy="3.5" r="3" fill="#fff"/><path d="M1 12c0-4 3-5.5 6-5.5s6 1.5 6 5.5z" fill="#fff"/></svg>My Account
</div>
<div class="abs util-box cart">
  <svg width="18" height="12" viewBox="0 0 18 12"><path d="M0 1h3l2 7h9l2-5H4.5" fill="none" stroke="#fff" stroke-width="1.2"/><circle cx="6.5" cy="10.5" r="1.2" fill="#fff"/><circle cx="12.5" cy="10.5" r="1.2" fill="#fff"/></svg>Cart is Empty
</div>
<span class="abs nav-flower"></span>
<nav>
  <a class="abs nav-item active" style="left:290px">Home</a>
  <a class="abs nav-item" style="left:330px">About Us</a>
  <a class="abs nav-item" style="left:387px">Products</a>
  <a class="abs nav-item" style="left:447px">Result Used Products</a>
  <a class="abs nav-item" style="left:559px">Contact Us</a>
</nav>

<div class="abs logo-card">
  <div class="logo-mark"></div>
  <div class="logo-name">Velvet Root<br>Studio</div>
</div>

<section class="abs hero" role="img" aria-label="Portrait of a woman with long dark waves and a jewelled earring over a soft grey damask backdrop"></section>
<h1 class="abs hero-title">Healthy Hair and Skin is our Priority... <strong>A Beautiful YOU is OUR specialty!!</strong></h1>
<svg class="abs hero-arrow" style="left:50px" width="20" height="38" viewBox="0 0 20 38"><path d="M18 1L2 19l16 18" fill="none" stroke="#fff" stroke-width="1.5"/></svg>
<svg class="abs hero-arrow" style="left:614px" width="20" height="38" viewBox="0 0 20 38"><path d="M2 1l16 18L2 37" fill="none" stroke="#fff" stroke-width="1.5"/></svg>

<section class="abs category-band"></section>
<div class="abs cat-card" style="left:75px">
  <div class="cat-photo" role="img" aria-label="Woman resting her chin on her hands beside skin care bottles" style="background:linear-gradient(135deg,#f6f1ee,#e6d6cc)"></div>
  <div class="cat-label">For Skin Care<i></i></div>
</div>
<div class="abs cat-card" style="left:257px">
  <div class="cat-photo" role="img" aria-label="Woman with natural curls holding a yellow flower" style="background:linear-gradient(135deg,#f4efea,#b88a66)"></div>
  <div class="cat-label">For Hair Care<i></i></div>
</div>
<div class="abs cat-card" style="left:438px">
  <div class="cat-photo" role="img" aria-label="White product bottles, tubes and jars" style="background:linear-gradient(135deg,#fafafa,#d9d9d9)"></div>
  <div class="cat-label">Our Products<i></i></div>
</div>

<div class="abs welcome-title"><span class="dot"></span><h2>Welcome To <span>Velvet Root Studio</span></h2></div>
<div class="abs welcome-rule"></div>
<p class="abs welcome-text">Lorem ipsum dolor sit amet, consectetuer adipiscing elit, sed diam nonummy nibh euismod tincidunt ut laoreet dolore magna aliquam erat volutpat. Ut wisi enim ad minim veniam, quis nostrud exerci tation ullamcorper suscipit lobortis nisl ut aliquip ex ea commodo consequat. Duis autem vel Lorem ipsum dolor sit amet, consectetuer adipiscing elit, sed diam nonummy nibh euismod tincidunt ...</p>
<div class="abs btn-more">Read More</div>
<div class="abs video" role="img" aria-label="Video tutorial still: woman holding a leaf beside a green serum bottle"></div>
<div class="abs video-bar"></div>
<svg class="abs video-play" width="26" height="30" viewBox="0 0 26 30"><path d="M2 2l22 13L2 28z" fill="rgba(255,255,255,.7)"/></svg>

<section class="abs reviews-band"></section>
<h3 class="abs reviews-title">Our Customer Review</h3>
<p class="abs reviews-sub">Lorem ipsum dolor sit amet, consectetur Donec a consequat mag &nbsp;Aenean eu velit &nbsp;Aenean sollicitudin</p>
<div class="abs rule-l"></div><div class="abs rule-r"></div>
<div class="abs stars">★★★</div>
<div class="abs quote-box"></div>
<svg class="abs quote-tail" width="18" height="10" viewBox="0 0 18 10"><path d="M0 0h18L9 10z" fill="#f4f2f0"/></svg>
<div class="abs quote-mark">“</div>
<p class="abs quote-text">Lorem sum dolor sit amet, consectetuer adipiscing elit, sed diam nonummy nibh euismod tincidunt ut laoreet re agn aliquam erat volutpat wisi enim ad minim veniam, quis nostrud exerci tation ullamcorper suscipit lobortis nisl ut aliquip modo consequat autem vel eum iriure dolor in hendrerit in vulputate velit esse molestie consequat, vel illum dolore eu.</p>
<div class="abs avatar" role="img" aria-label="Customer portrait"></div>
<div class="abs quote-name">Lorem Ipsum, DOLOR</div>

<div class="abs feature" style="left:75px">
  <svg width="46" height="30" viewBox="0 0 46 30"><rect x="14" y="8" width="20" height="14" fill="#4a403b"/><path d="M34 12h6l4 5v5H34z" fill="#4a403b"/><circle cx="19" cy="25" r="3" fill="#4a403b"/><circle cx="38" cy="25" r="3" fill="#4a403b"/><path d="M2 10h10M4 15h8M6 20h6" stroke="#4a403b" stroke-width="2"/></svg>
  <span>Enjoy Everyday<br>Free Shipping</span>
</div>
<div class="abs feature" style="left:257px">
  <svg width="36" height="28" viewBox="0 0 36 28"><path d="M18 6C13 2 6 2 2 4v20c4-2 11-2 16 2 5-4 12-4 16-2V4c-4-2-11-2-16 2z" fill="#4a403b"/><path d="M18 6v20" stroke="#ececec" stroke-width="1.2"/></svg>
  <span>Request a<br>Free Catalog</span>
</div>
<div class="abs feature gift" style="left:438px">
  <svg width="36" height="26" viewBox="0 0 36 26"><rect x="1" y="1" width="34" height="24" rx="2" fill="none" stroke="#4a403b" stroke-width="1.6"/><path d="M1 8h34M12 1v24" stroke="#4a403b" stroke-width="1.6"/></svg>
  <span>E-Gift<br>Cards</span>
</div>

<footer class="abs footer"></footer>
<div class="abs footer-panel"></div>
<div class="abs news-box"></div>
<h4 class="abs news-title">LATEST NEWS</h4>
<div class="abs news-rule"></div>
<div class="abs news-date">24-01-2015</div>
<div class="abs news-lead">Lorem ipsum dolor sit amet, consectetuer adipiscing</div>
<div class="abs news-text">Lorem ipsum dolor sit amet, consectetuer adipiscing elit,</div>
<div class="abs news-more">Read More</div>

<div class="abs promo-strip"></div>
<div class="abs promo" style="left:292px" role="img" aria-label="Skin care offer photo"><div class="promo-inner"><b>25<small>%</small> OFF</b><span>For Skin Care</span></div></div>
<div class="abs promo" style="left:401px" role="img" aria-label="Hair care offer photo"><div class="promo-inner"><b>30<small>%</small> OFF</b><span>For Hair Care</span></div></div>
<div class="abs promo" style="left:509px" role="img" aria-label="Products offer photo"><div class="promo-inner"><b>10 <small>%</small> OFF</b><span>Our Products</span></div></div>

<div class="abs col-title" style="left:85px;top:1055px">Newsletter</div>
<div class="abs newsletter-input">Enter your e-mail</div>
<div class="abs newsletter-go">GO</div>
<div class="abs col-title" style="left:85px;top:1098px">Store Information</div>
<svg class="abs" style="left:87px;top:1118px" width="8" height="12" viewBox="0 0 8 12"><path d="M4 0a4 4 0 0 1 4 4c0 3-4 8-4 8S0 7 0 4a4 4 0 0 1 4-4z" fill="#fff"/><circle cx="4" cy="4" r="1.5" fill="#4a403b"/></svg>
<div class="abs store-line" style="left:101px;top:1119px">Lorem ipsum dolor sit amet consectetu<br>adipiscing elit sed diam</div>
<svg class="abs" style="left:87px;top:1143px" width="10" height="8" viewBox="0 0 10 8"><rect x=".5" y=".5" width="9" height="7" fill="none" stroke="#fff"/><path d="M.5 .5L5 4.5 9.5 .5" fill="none" stroke="#fff"/></svg>
<div class="abs store-line" style="left:101px;top:1143px">info@velvetrootstudio.com</div>

<div class="abs col-title" style="left:289px;top:1063px">Quick Links</div>
<ul class="abs links" style="left:289px;top:1092px"><li style="margin-bottom:9px">HOME</li><li style="margin-bottom:9px">ABOUT US</li><li>PRODUCTS</li></ul>
<ul class="abs links" style="left:347px;top:1092px"><li style="margin-bottom:5px">RESULT USED<br>PRODUCTS</li><li>CONTACT US</li></ul>
<div class="abs col-title" style="left:431px;top:1063px">My Account</div>
<ul class="abs links" style="left:428px;top:1093px"><li style="margin-bottom:9px">My Orders</li><li style="margin-bottom:9px">My Merchandise Returns</li><li>My Credit Slips</li></ul>
<ul class="abs links" style="left:534px;top:1093px"><li style="margin-bottom:9px">My Addresses</li><li style="margin-bottom:9px">My Personal Info</li><li>My Vouchers</li></ul>

<div class="abs footer-rule"></div>
<div class="abs copyright">© 2015 Velvet Root Studio. All Rights Reserved.</div>
<div class="abs pay" style="left:467px">Tallo</div>
<div class="abs pay" style="left:494px">Tallo</div>
<div class="abs pay" style="left:521px">Orbi</div>
<div class="abs pay" style="left:548px">Zenpay</div>
<div class="abs pay" style="left:575px;width:30px">CoinPouch</div>

</body>
</html>
```